Signage for a store*

logo on the two sides of the sign
in the middle is the name of the store witch is VORELT
at the bottom of the two logos, one side for location/address and the other side is contact details phone number is 718-392-6107 address is 2974 THE SIGN WILL BEE 15 FEET BY 4 FEET I WOULD LIKE THAT THE
BACKGROUND OF THE SIGN SHOULD HAVE A NICE COLOR BASE
THAT GOES FOR A WINE STORE

```html
<!DOCTYPE html>
<html lang="en">
<head>
<meta charset="utf-8">
<title>VORELT – Store Sign</title>
<link rel="stylesheet" href="https://fonts.googleapis.com/css2?family=Libre+Baskerville:wght@400&family=Jost:wght@600&display=swap">
<style>
  :root {
    --page-bg: #e3e3e5;
    --wine-light: #a11d2c;
    --wine-mid: #8a1422;
    --wine-dark: #660a16;
    --gold: #d9bf8c;
    --name-white: #ffffff;
    --detail-pink: #efd9de;
  }
  html, body {
    margin: 0;
    width: 1200px;
    height: 424px;
    overflow: hidden;
    background: var(--page-bg);
  }
  .sign {
    position: absolute;
    left: 71px;
    top: 51px;
    width: 1058px;
    height: 282px;
    background: radial-gradient(ellipse 60% 75% at 58% 52%, var(--wine-light) 0%, var(--wine-mid) 55%, var(--wine-dark) 100%);
    overflow: hidden;
  }
  .brand-mark {
    position: absolute;
    left: 115px;
    top: 60px;
    width: 160px;
    text-align: center;
  }
  .brand-mark__dot {
    display: block;
    width: 22px;
    height: 22px;
    margin: 0 auto 14px;
    border: 2px solid var(--gold);
    border-radius: 50%;
    box-sizing: border-box;
  }
  .brand-mark__name {
    font-family: "Libre Baskerville", serif;
    font-size: 31px;
    color: var(--gold);
    letter-spacing: 1px;
    line-height: 1;
  }
  .store-name {
    position: absolute;
    left: 312px;
    top: 40px;
    width: 690px;
    margin: 0;
    text-align: right;
    font-family: "Libre Baskerville", serif;
    font-weight: 400;
    font-size: 158px;
    line-height: 1;
    letter-spacing: -4px;
    color: var(--name-white);
  }
  .divider {
    position: absolute;
    left: 346px;
    top: 202px;
    width: 582px;
    height: 2px;
    background: var(--gold);
  }
  .divider__dot {
    position: absolute;
    left: 731px;
    top: 192px;
    width: 20px;
    height: 20px;
    border: 2px solid var(--gold);
    border-radius: 50%;
    background: var(--wine-mid);
    box-sizing: border-box;
  }
  .details {
    position: absolute;
    top: 209px;
    margin: 0;
    font-family: "Jost", sans-serif;
    font-weight: 600;
    font-size: 23px;
    line-height: 1.2;
    color: var(--detail-pink);
    white-space: nowrap;
  }
  .details--address { left: 346px; }
  .details--phone { right: 130px; }
</style>
</head>
<body>
  <div class="sign">
    <div class="brand-mark">
      <span class="brand-mark__dot"></span>
      <div class="brand-mark__name">VORELT</div>
    </div>
    <h1 class="store-name">VORELT</h1>
    <div class="divider"></div>
    <div class="divider__dot"></div>
    <p class="details details--address">2974 Kessler Ave. Brooklyn, N.Y. 11231</p>
    <p class="details details--phone">718-392-6107</p>
  </div>
</body>
</html>
```